A5 Personal trainer profile for brackmoor wellness

I need a A5 Landscape profile designed for the company I work for. Company name is Brackmoor Wellness. The profile is for personal trainers to let people know:

1. Brief description of themselves
2. Qualifications

A picture will be required on the right hand side of the profile. Brackmoor Wellness colours are green and white.

The Brackmoor Wellness Logo in the boarder of the example included must remain. We are looking for a clinical and professional design.

Industry/Entity Type

Health

```html
<!DOCTYPE html>
<html lang="en">
<head>
<meta charset="utf-8">
<title>Personal Trainer Profile – Brackmoor Wellness</title>
<link href="https://fonts.googleapis.com/css2?family=Roboto+Condensed:wght@700&family=Source+Sans+3:ital,wght@0,400;0,600;1,400&display=swap" rel="stylesheet">
<style>
  :root {
    --green: #2e9a3a;
    --green-dark: #1d7a2c;
    --green-light: #4cb848;
    --grey-text: #5a5a5a;
    --body-text: #2b2b2b;
    --white: #ffffff;
    --paper: #f4f5f4;
  }
  * { box-sizing: border-box; margin: 0; padding: 0; }
  html, body { width: 1200px; height: 877px; overflow: hidden; background: var(--paper); }
  .profile {
    position: relative; width: 1200px; height: 877px;
    background: linear-gradient(100deg, var(--white) 55%, #e9ebea 100%);
    font-family: "Source Sans 3", sans-serif; color: var(--body-text);
  }
  .role {
    position: absolute; left: 26px; top: 48px;
    font: 700 68px/1 "Roboto Condensed", sans-serif; color: var(--grey-text);
  }
  .trainer-name {
    position: absolute; left: 24px; top: 138px;
    font: 700 90px/1 "Roboto Condensed", sans-serif; color: var(--green-dark);
    letter-spacing: 1px;
  }
  .feature-photo {
    position: absolute; left: 566px; top: 20px; width: 214px; height: 214px;
    border-radius: 50%; border: 10px solid var(--green);
    box-shadow: 0 0 0 4px var(--white), 0 0 0 7px #bcd9bd;
    background: radial-gradient(circle at 50% 45%, #6b5448 0%, #3a2b24 55%, #141010 100%);
  }
  .trainer-photo {
    position: absolute; left: 798px; top: 12px; width: 382px; height: 421px;
    background: linear-gradient(180deg, #ffffff 0%, #f1f3f1 40%, #9bd35a 62%, #86c64a 100%);
  }
  .banner {
    position: absolute; color: var(--white);
    font-family: "Source Sans 3", sans-serif; font-weight: 600;
    background: linear-gradient(180deg, var(--green-light), var(--green-dark));
    display: flex; align-items: center;
  }
  .banner--qualifications {
    left: 0; top: 288px; width: 364px; height: 52px; padding-left: 42px;
    font-size: 32px; text-transform: uppercase;
    clip-path: polygon(0 0, 93% 0, 100% 50%, 93% 100%, 0 100%);
  }
  .banner--help {
    left: 715px; top: 433px; width: 485px; height: 58px; padding-left: 60px;
    font-size: 38px; font-weight: 400;
    clip-path: polygon(7% 0, 100% 0, 100% 100%, 7% 100%, 0 50%);
  }
  .qualification-list {
    position: absolute; left: 52px; top: 370px; width: 580px; list-style: none;
    font-size: 22px; line-height: 28px;
  }
  .qualification-list li { position: relative; padding-left: 32px; margin-bottom: 7px; }
  .bullet {
    position: absolute; width: 17px; height: 17px; border-radius: 50%;
    background: radial-gradient(circle at 35% 35%, #9fe08f, var(--green) 55%, var(--green-dark));
    box-shadow: 0 0 0 2px #d9ead9;
  }
  .qualification-list .bullet { left: 0; top: 6px; }
  .help-list {
    position: absolute; right: 48px; top: 512px; list-style: none;
    font-size: 22px; line-height: 28px; text-align: right;
  }
  .help-list li { position: relative; padding-right: 34px; margin-bottom: 8px; }
  .help-list .bullet { right: 0; top: 6px; }
  .brand {
    position: absolute; left: 38px; top: 616px; display: flex; align-items: center; gap: 14px;
  }
  .brand-mark { width: 44px; height: 44px; background: var(--green); }
  .brand-name {
    font: 600 50px/1 "Source Sans 3", sans-serif; color: var(--green);
  }
  .testimonial-band {
    position: absolute; left: 0; top: 730px; width: 1200px; height: 112px;
    background: linear-gradient(90deg, var(--green-light) 0%, var(--green) 50%, var(--green-dark) 100%);
  }
  .testimonial-tab {
    position: absolute; left: 38px; top: 705px; width: 424px; height: 54px;
    padding-left: 22px; display: flex; align-items: center;
    background: linear-gradient(180deg, #2b8d36, #1a6b26);
    color: var(--white); font-size: 28px; font-weight: 600;
    clip-path: polygon(0 0, 100% 0, 100% 100%, 0 100%);
    box-shadow: 0 3px 6px rgba(0,0,0,.25);
  }
  .testimonial {
    position: absolute; left: 34px; top: 773px; width: 1140px;
    color: var(--white); font-size: 19.5px; line-height: 25px; font-style: italic;
  }
  .testimonial cite { font-style: normal; font-weight: 600; margin-left: 110px; }
</style>
</head>
<body>
<main class="profile">
  <h2 class="role">Personal Trainer</h2>
  <h1 class="trainer-name">DANIEL OFORI</h1>

  <div class="feature-photo" role="img" aria-label="Close-up photo of toned abdominal muscles"></div>
  <div class="trainer-photo" role="img" aria-label="Photo of the personal trainer smiling in a green polo shirt"></div>

  <div class="banner banner--qualifications">Qualifications</div>
  <ul class="qualification-list">
    <li><span class="bullet"></span>Advanced Circuit Training</li>
    <li><span class="bullet"></span>Advanced Diploma in Personal Training -<br>Level 3 REPS Registered</li>
    <li><span class="bullet"></span>Fitness Instructor - Level 2 REPS Registered</li>
    <li><span class="bullet"></span>Also qualified in – Suspension training, Studio Cycling, Sports<br>Nutrition, Weight Management</li>
  </ul>

  <div class="banner banner--help">How I can help you?</div>
  <ul class="help-list">
    <li>Reduce body fat&nbsp; and increase body definition<span class="bullet"></span></li>
    <li>Increase stamina, improve agility and speed<span class="bullet"></span></li>
    <li>Increase strength and size<span class="bullet"></span></li>
    <li>Plyometric training and conditioning<span class="bullet"></span></li>
    <li>Flexibility and core strength<span class="bullet"></span></li>
  </ul>

  <div class="brand">
    <span class="brand-mark"></span>
    <span class="brand-name">Brackmoor Wellness</span>
  </div>

  <div class="testimonial-band"></div>
  <div class="testimonial-tab">What my clients say about me?</div>
  <p class="testimonial">"With Daniel my training is always challenging and fun. I don't remember a session to be boring or repetitive. In short time I improved my core strength and flexibility. I can run 10k without stopping. It is amazing improvement." <cite>- Laura Pembridge</cite></p>
</main>
</body>
</html>
```